Summer Special for Harbourline Gym

Running a 12 month special starting from 1st Jan 2019. I already have the image (see below), I just need the font and layout to have a summer feel and to be eye catching. Format required is for a Facebook cover, Instagram, if possible the one image but spread across 3 tiles on the homepage and a format for a poster .

"SUMMER SPECIAL
12 months from
$350.00
SAVE OVER 20%"
"Terms and conditions apply"

Attached is the photo for the current promo, a logo we generally use and another special we have run in the past to assist you

Target Market(s)

18 - 45 male and female

Industry/Entity Type

Fitness

Font styles to use
Sans Serif
Script

Colors

Designer to choose colors to be used in the design.

Requirements
Must have
• The main emphasis would be on the Summer font/text (special) and the layout of the text. If we can add some brighter colors to the layout that would be great just to capture their attention. If there's any effects you want to add to it that would be great. The logo can be faint in the background.
• "SUMMER SPECIAL
• 12 months from
• $350.00
• SAVE OVER 20%"
• "Terms and conditions apply"
• All contact details, address, website, etc which will be supplied
Nice to have
• Some artistic effects to catch your eye and enhance the professionalism of the designer

```html
<!DOCTYPE html>
<html lang="en">
<head>
<meta charset="utf-8">
<title>Harbourline Gym – Summer Special Covers</title>
<link href="https://fonts.googleapis.com/css2?family=Staatliches&family=Cinzel:wght@600&display=swap" rel="stylesheet">
<style>
  :root {
    --stage: #474747;
    --yellow: #f9c21b;
    --red: #b5161b;
    --red-deep: #9c1014;
    --ink: #1d1d1d;
    --light: #d3d8da;
    --dark: #2a2a2a;
    --white: #ffffff;
    --steel: #8d8f91;
  }
  * { margin: 0; padding: 0; box-sizing: border-box; }
  html, body { width: 1200px; height: 883px; overflow: hidden; background: var(--stage); }
  .stage { position: relative; width: 1200px; height: 883px; }
  .cover { position: absolute; left: 100px; width: 1000px; height: 381px; overflow: hidden; font-family: "Staatliches", "Impact", sans-serif; }
  .cover--light { top: 18px; background: linear-gradient(100deg, #c4cbce 0%, var(--light) 55%, #c8cfd1 100%); }
  .cover--dark { top: 462px; background: radial-gradient(ellipse at 35% 45%, #3a3a3a 0%, var(--dark) 55%, #1c1c1c 100%); }
  .version-label { position: absolute; left: 0; width: 1200px; text-align: center; color: var(--white); font-family: "Cinzel", serif; font-size: 22px; letter-spacing: 2px; }
  .version-label--one { top: 412px; }
  .version-label--two { top: 852px; }

  .headline { position: absolute; color: var(--yellow); font-size: 88px; line-height: 1; letter-spacing: 2px; text-shadow: 3px 3px 0 #6b4d00; white-space: nowrap; }
  .offer { position: absolute; font-size: 56px; line-height: 1; white-space: nowrap; }
  .price-tag { position: absolute; background: var(--red); color: var(--white); font-size: 46px; line-height: 1; padding: 4px 28px 4px 26px; clip-path: polygon(0 0, 100% 0, 92% 100%, 0 100%); white-space: nowrap; }
  .save-band { position: absolute; left: 0; background: var(--yellow); clip-path: polygon(0 0, 100% 0, 93% 100%, 0 100%); }
  .save-band span { position: absolute; color: var(--ink); font-size: 66px; letter-spacing: 11px; line-height: 1; white-space: nowrap; }
  .photo { position: absolute; }
  .brand-disc { position: absolute; border-radius: 50%; background: #111; display: flex; align-items: center; justify-content: center; text-align: center; color: var(--white); line-height: 1.05; }
  .terms { position: absolute; color: var(--ink); line-height: 1.05; }

  /* Version 1 */
  .cover--light .headline { left: 45px; top: 60px; }
  .cover--light .offer { left: 45px; top: 150px; color: var(--red); }
  .cover--light .price-tag { left: 460px; top: 154px; }
  .cover--light .save-band { top: 232px; width: 648px; height: 80px; }
  .cover--light .save-band span { left: 45px; top: 8px; }
  .cover--light .photo { left: 660px; top: 0; width: 240px; height: 381px; background: linear-gradient(180deg, #2a2a2a 0%, #8a5a44 22%, #a5694f 55%, #c9472f 78%, #b43a28 100%); border-radius: 90px 90px 0 0; }
  .cover--light .brand-disc { left: 868px; top: 2px; width: 136px; height: 136px; font-size: 22px; }
  .cover--light .terms { left: 905px; top: 298px; width: 92px; font-size: 16px; line-height: 1; }

  /* Version 2 */
  .cover--dark .diagonals { position: absolute; inset: 0; }
  .cover--dark .headline { left: 32px; top: 82px; }
  .cover--dark .offer { left: 32px; top: 178px; color: var(--white); }
  .cover--dark .price-tag { left: 392px; top: 180px; }
  .cover--dark .save-band { top: 250px; width: 505px; height: 68px; }
  .cover--dark .save-band span { left: 32px; top: 4px; font-size: 58px; }
  .cover--dark .photo { left: 770px; top: 0; width: 230px; height: 381px; background: linear-gradient(180deg, #222 0%, #8a5a44 20%, #a5694f 55%, #c9472f 80%, #b43a28 100%); border-radius: 80px 80px 0 0; }
  .cover--dark .brand-disc { left: 560px; top: 8px; width: 126px; height: 126px; font-size: 20px; border: 4px solid #2f2f2f; }
  .cover--dark .terms { left: 525px; top: 346px; font-size: 17px; color: #222; white-space: nowrap; }
</style>
</head>
<body>
<main class="stage">

  <section class="cover cover--light" aria-label="Summer special cover, light version">
    <div class="photo" role="img" aria-label="Photo of a muscular athlete in a black cap and red shorts"></div>
    <div class="brand-disc">HARBOURLINE<br>GYM</div>
    <h1 class="headline">SUMMER SPECIAL</h1>
    <p class="offer">12 MONTHS FROM</p>
    <p class="price-tag">$350.00</p>
    <div class="save-band"><span>SAVE OVER 20%</span></div>
    <p class="terms">***<br>TERMS AND<br>CONDITIONS<br>APPLY***</p>
  </section>
  <p class="version-label version-label--one">VERSION 1</p>

  <section class="cover cover--dark" aria-label="Summer special cover, dark version">
    <svg class="diagonals" viewBox="0 0 1000 381" preserveAspectRatio="none" aria-hidden="true">
      <polygon points="900,0 1000,0 1000,381 460,381" fill="var(--light)"/>
      <polygon points="840,38 878,38 480,381 440,381" fill="var(--red-deep)"/>
      <polygon points="720,100 840,38 440,381 395,381 640,175" fill="var(--steel)" opacity="0.85"/>
      <polygon points="600,190 700,115 725,115 620,205" fill="var(--red)"/>
    </svg>
    <div class="photo" role="img" aria-label="Photo of a muscular athlete in a black cap and red shorts"></div>
    <div class="brand-disc">HARBOURLINE<br>GYM</div>
    <h1 class="headline">SUMMER SPECIAL</h1>
    <p class="offer">12 MONTHS FROM</p>
    <p class="price-tag">$350.00</p>
    <div class="save-band"><span>SAVE OVER 20%</span></div>
    <p class="terms">***TERMS AND CONDITIONS APPLY***</p>
  </section>
  <p class="version-label version-label--two">VERSION 2</p>

</main>
</body>
</html>
```